BrPeople Business Cards for SME Experts

We need a business card for a new company based in Clearwater FL called Brightfold of People. BrP is your access to on-demand subject matter experts. The final design should be very clean communicating innovation and expertise. Our logo design is attached.

The Information Age has affected the workforce in that automation and computerization have resulted in higher productivity coupled with net job loss of many knowledgeable employees. Combined with the creation of the internet and search capabilities, the disintermediation of the value chain of Subject Matter Experts (SME) has happened. We no longer need to work through traditional consulting firms for all consulting needs, instead the direct access to the SME, through a leaner and lower cost model is what the market is demanding.
BrPeople is a new marketplace to buy consulting services. The business model is that all consultants (subject matter experts) can become a consulting resource in the marketplace following our guidelines. The consumer can now easily access consultants that they could not find easily before.
In much the way an Zaxo car can be identified and requested, so can a BrPeople Consultant. Each consultant can be identified by: location, expertise, billing rate, and prior experience rating.
By seamlessly connecting consultants to requesters through a new Brightfold of People marketplace, you now will have an easy to use and quicker turnaround to request and staff your consulting needs. Leveraging the BrP app, you can access the subject matter expert you need for your business requirement.

Target Market(s)

Small and medium sized companies; non-profits

Industry/Entity Type

Business Consultant

Contact Information for Business Card

Name
website
email address
Logo
mailing address (debating if I really need...)
twitter
LinkedIn

Requirements
Must have
• the logo I have included in the design; want the colors to be consistent with the logo design

```html
<!DOCTYPE html>
<html lang="en">
<head>
<meta charset="utf-8">
<title>Brightfold of People – Business Card</title>
<link rel="stylesheet" href="https://fonts.googleapis.com/css2?family=Ubuntu:wght@500;700&family=Open+Sans:wght@400;600&display=swap">
<style>
  :root {
    --navy: #26286e;
    --navy-light: #3a3d8a;
    --cyan: #1aa6cf;
    --white: #ffffff;
    --backdrop: #e4e6ec;
  }
  html, body {
    margin: 0;
    width: 1200px;
    height: 1000px;
    overflow: hidden;
    background: var(--backdrop);
  }
  .card {
    position: absolute;
    left: 150px;
    top: 243px;
    width: 900px;
    height: 514px;
    border-radius: 24px;
    overflow: hidden;
    background: var(--white);
    box-shadow: 0 10px 30px rgba(20, 22, 60, 0.18);
  }
  .card__art { position: absolute; inset: 0; }
  .brand {
    position: absolute;
    left: 80px;
    top: 150px;
    display: flex;
    flex-direction: column;
    align-items: flex-start;
    gap: 22px;
  }
  .brand__mark {
    width: 110px;
    height: 110px;
    border-radius: 50%;
    border: 6px solid var(--cyan);
    box-sizing: border-box;
  }
  .brand__name {
    font-family: "Ubuntu", sans-serif;
    font-weight: 700;
    font-size: 38px;
    color: var(--navy);
    margin: 0;
  }
  .person {
    position: absolute;
    right: 40px;
    top: 28px;
    text-align: right;
  }
  .person__name {
    font-family: "Ubuntu", sans-serif;
    font-weight: 700;
    font-size: 34px;
    color: var(--navy);
    margin: 0;
    line-height: 1.05;
  }
  .person__role {
    font-family: "Open Sans", sans-serif;
    font-weight: 600;
    font-size: 20px;
    color: var(--cyan);
    margin: 0;
  }
  .contact {
    position: absolute;
    right: 40px;
    top: 178px;
    text-align: right;
    font-family: "Open Sans", sans-serif;
    font-size: 21px;
    color: var(--white);
    line-height: 30px;
  }
  .contact__icons {
    display: flex;
    justify-content: flex-end;
    gap: 6px;
    margin-bottom: 10px;
  }
  .contact__icon {
    width: 24px;
    height: 24px;
    border-radius: 4px;
    background: var(--cyan);
    display: block;
  }
  .contact__line { margin: 0; }
  .contact__address {
    margin-top: 6px;
    display: flex;
    justify-content: flex-end;
    gap: 10px;
    align-items: flex-start;
  }
  .contact__address-text { margin: 0; text-align: right; }
  .contact__pin { flex: none; margin-top: 3px; }
</style>
</head>
<body>
  <div class="card">
    <svg class="card__art" viewBox="0 0 900 514" width="900" height="514" aria-hidden="true">
      <defs>
        <linearGradient id="wave-sheen" x1="0" y1="1" x2="1" y2="0">
          <stop offset="0" stop-color="#5a5d9e"/>
          <stop offset="0.5" stop-color="#2f3278"/>
          <stop offset="1" stop-color="#26286e"/>
        </linearGradient>
      </defs>
      <path class="wave wave--cyan" fill="#1aa6cf" transform="translate(-34 -20)"
            d="M340 534 C470 490 520 330 620 250 C720 170 820 140 940 100 L940 560 Z"/>
      <path class="wave wave--gap" fill="#ffffff" transform="translate(-22 -13)"
            d="M340 534 C470 490 520 330 620 250 C720 170 820 140 940 100 L940 560 Z"/>
      <path class="wave wave--navy" fill="#26286e"
            d="M340 534 C470 490 520 330 620 250 C720 170 820 140 940 100 L940 560 Z"/>
      <path class="wave wave--sheen" fill="url(#wave-sheen)" opacity="0.7"
            d="M360 534 C470 500 520 380 600 300 C650 250 680 330 560 534 Z"/>
    </svg>

    <div class="brand">
      <span class="brand__mark"></span>
      <p class="brand__name">Brightfold of People</p>
    </div>

    <div class="person">
      <p class="person__name">John Doe</p>
      <p class="person__role">Owner</p>
    </div>

    <div class="contact">
      <div class="contact__icons">
        <svg class="contact__icon" viewBox="0 0 24 24" role="img" aria-label="website">
          <rect width="24" height="24" rx="4" fill="#1aa6cf"/>
          <circle cx="12" cy="12" r="7" fill="none" stroke="#26286e" stroke-width="1.8"/>
          <path d="M5 12h14M12 5c-3 4-3 10 0 14M12 5c3 4 3 10 0 14" fill="none" stroke="#26286e" stroke-width="1.5"/>
        </svg>
        <svg class="contact__icon" viewBox="0 0 24 24" role="img" aria-label="email">
          <rect width="24" height="24" rx="4" fill="#1aa6cf"/>
          <rect x="5" y="7" width="14" height="10" fill="none" stroke="#26286e" stroke-width="1.8"/>
          <path d="M5 7l7 6 7-6" fill="none" stroke="#26286e" stroke-width="1.8"/>
        </svg>
        <span class="contact__icon" role="img" aria-label="social profile"></span>
        <span class="contact__icon" role="img" aria-label="professional profile"></span>
      </div>
      <p class="contact__line">www.website.com</p>
      <p class="contact__line">info@email.com</p>
      <p class="contact__line">@yourhandle</p>
      <p class="contact__line">yourprofile</p>
      <div class="contact__address">
        <p class="contact__address-text">Harbor Pine Drive<br>Bayview, FL 12345</p>
        <svg class="contact__pin" width="24" height="24" viewBox="0 0 24 24" role="img" aria-label="address">
          <rect width="24" height="24" rx="4" fill="#1aa6cf"/>
          <path d="M12 19s-5-5.5-5-9a5 5 0 0 1 10 0c0 3.5-5 9-5 9z" fill="#26286e"/>
          <circle cx="12" cy="10" r="2" fill="#1aa6cf"/>
        </svg>
      </div>
    </div>
  </div>
</body>
</html>
```